Emergency Dental Referral Company

I need a brochure to advertise my business to prospective dentists that may want to join or to dentists that may want to use this for their own patients. I also need to advertise this brochure to ER physicians who see many dental emergencies. This brochure is meant to be dual purpose: advertise our company and services to the ER physicians who then hand out the brochures to the dental emergency patients in pain. See our website for further details at www.molarrelieffast.net

I will also be attaching our logo design.

Target Market(s)

Emergency Room physicians and other medical personnel who will distribute these brochures to patients in dental pain and dental emergencies

Industry/Entity Type

Business

Font styles to use
Serif
Sans Serif

Requirements
Must have
• Must be simple! Must have a call to action- inspiration to go to website. Highlight our guarantee that states "If you are not seen by a dentist in 24 hours or less, you will receive your money back. Emphasis on the logo. Must discuss how we find a dentist in your zip code in three easy steps.
• For the color- please make similar to our website of www.molarrelieffast.net
Nice to have
• Would like to state that this service can see patients at any hour of the day.
Should not have
• no contact information besides the URL. www.molarrelieffast.net

```html
<!DOCTYPE html>
<html lang="en">
<head>
<meta charset="utf-8">
<title>Molar Relief Fast – Emergency Dentist Brochure</title>
<link rel="stylesheet" href="https://fonts.googleapis.com/css2?family=Source+Sans+3:wght@400;600;700&display=swap">
<style>
  :root {
    --page-bg: #e6e6e6;
    --brand-blue: #0b6fc4;
    --brand-blue-dark: #0a58a3;
    --brand-green: #2fa83c;
    --paper: #f7f7f7;
    --paper-shade: #e9e9e9;
    --white: #ffffff;
    --photo-light: #efe6df;
    --photo-mid: #c9a796;
  }
  * { box-sizing: border-box; margin: 0; padding: 0; }
  html, body {
    width: 1200px;
    height: 625px;
    overflow: hidden;
    background: var(--page-bg);
    font-family: "Source Sans 3", Arial, sans-serif;
  }
  .brochure {
    position: absolute;
    left: 180px;
    top: 16px;
    width: 610px;
    height: 430px;
    transform: scale(1.377);
    transform-origin: top left;
    overflow: hidden;
    background: linear-gradient(180deg, var(--paper) 0%, var(--white) 40%, var(--paper-shade) 100%);
  }
  .brochure-shapes { position: absolute; inset: 0; z-index: 0; }
  .hero-photo {
    position: absolute;
    left: 22px;
    top: 146px;
    width: 140px;
    height: 86px;
    z-index: 1;
    border-radius: 6px 6px 0 0;
    background: radial-gradient(ellipse at 45% 45%, var(--photo-mid) 0%, var(--photo-light) 65%, rgba(255,255,255,0) 95%);
  }
  .brand-mark {
    position: absolute;
    z-index: 2;
    display: flex;
    align-items: center;
    justify-content: center;
    gap: 6px;
    color: var(--brand-blue-dark);
    font-weight: 700;
    white-space: nowrap;
  }
  .brand-mark__square { background: var(--brand-green); display: inline-block; }
  .brand-mark--main { left: 50px; width: 210px; top: 52px; font-size: 20px; }
  .brand-mark--main .brand-mark__square { width: 16px; height: 16px; }
  .brand-mark--small { left: 393px; width: 120px; top: 174px; font-size: 12px; gap: 4px; }
  .brand-mark--small .brand-mark__square { width: 10px; height: 10px; }
  .headline-emergency {
    position: absolute;
    z-index: 2;
    left: 50px;
    top: 92px;
    width: 210px;
    text-align: center;
    color: var(--brand-green);
    font-weight: 700;
    font-size: 20px;
    line-height: 25px;
  }
  .step {
    position: absolute;
    z-index: 2;
    top: 28px;
    width: 100px;
    text-align: center;
  }
  .step__title { color: var(--brand-blue-dark); font-weight: 700; font-size: 16px; line-height: 18px; }
  .step__text { color: var(--brand-green); font-size: 12px; line-height: 13px; margin-top: 2px; }
  .step--one { left: 308px; }
  .step--two { left: 398px; }
  .step--three { left: 494px; }
  .banner-text {
    position: absolute;
    z-index: 2;
    color: var(--white);
    font-weight: 700;
    white-space: nowrap;
  }
  .banner-text--find { left: 56px; top: 243px; font-size: 18px; }
  .banner-text--steps { left: 34px; top: 284px; font-size: 34px; letter-spacing: 0.5px; }
  .guarantee {
    position: absolute;
    z-index: 2;
    left: 10px;
    top: 342px;
    width: 300px;
    text-align: center;
    color: var(--white);
    font-weight: 700;
    font-size: 18px;
    line-height: 20px;
  }
  .guarantee__or { font-size: 15px; }
  .website-cta {
    position: absolute;
    z-index: 2;
    left: 330px;
    top: 313px;
    width: 260px;
    text-align: center;
    color: var(--white);
  }
  .website-cta__lead { font-size: 11.5px; letter-spacing: 0.1px; }
  .website-cta__url { font-size: 15px; font-weight: 600; margin-top: 3px; }
</style>
</head>
<body>
  <main class="brochure">
    <svg class="brochure-shapes" viewBox="0 0 610 430" width="610" height="430" aria-hidden="true">
      <defs>
        <linearGradient id="top-band" x1="0" x2="1" y1="0" y2="0">
          <stop offset="0" stop-color="#0b6fc4"/>
          <stop offset="0.6" stop-color="#3597e0"/>
          <stop offset="1" stop-color="#0b6fc4"/>
        </linearGradient>
        <radialGradient id="step-disc" cx="0.4" cy="0.35" r="0.7">
          <stop offset="0" stop-color="#3a9ae6"/>
          <stop offset="1" stop-color="#0a5aa8"/>
        </radialGradient>
      </defs>
      <rect class="top-band" x="0" y="0" width="610" height="15" fill="url(#top-band)"/>
      <path class="swoosh-green" d="M0,222 C200,236 420,206 610,150 L610,170 C420,222 200,246 0,236 Z" fill="#3db34a"/>
      <path class="swoosh-blue" d="M0,234 C200,244 420,220 610,164 L610,430 L0,430 Z" fill="#0b6fc4"/>

      <g class="step-icons">
        <circle cx="358" cy="109" r="27" fill="url(#step-disc)"/>
        <path d="M346,109 l8,8 l15,-16" fill="none" stroke="#fff" stroke-width="5" stroke-linecap="round" stroke-linejoin="round"/>
        <circle cx="448" cy="109" r="27" fill="url(#step-disc)"/>
        <path d="M436,109 l8,8 l15,-16" fill="none" stroke="#fff" stroke-width="5" stroke-linecap="round" stroke-linejoin="round"/>
        <circle cx="544" cy="109" r="27" fill="url(#step-disc)"/>
        <path d="M532,109 l8,8 l15,-16" fill="none" stroke="#fff" stroke-width="5" stroke-linecap="round" stroke-linejoin="round"/>
        <path d="M393,109 h14 m-5,-4 l5,4 l-5,4" fill="none" stroke="#2fa83c" stroke-width="3"/>
        <path d="M486,109 h14 m-5,-4 l5,4 l-5,4" fill="none" stroke="#2fa83c" stroke-width="3"/>
      </g>

      <polygon class="banner-find" points="14,256 30,238 256,238 256,272 30,272" fill="#2fa83c"/>
      <polygon class="banner-steps-fold" points="20,282 30,282 30,340 20,332" fill="#1f7d2a"/>
      <polygon class="banner-steps" points="22,282 282,282 302,306 282,330 22,330" fill="#3db34a"/>
    </svg>

    <div class="hero-photo" role="img" aria-label="Photo of a smiling woman pointing upward"></div>

    <div class="brand-mark brand-mark--main">
      <span class="brand-mark__square"></span>
      <span class="brand-mark__name">Molar Relief Fast</span>
    </div>
    <h1 class="headline-emergency">YOUR EMERGENCY<br>DENTIST</h1>

    <section class="step step--one">
      <h2 class="step__title">STEP-1</h2>
      <p class="step__text">Fill Out Form</p>
    </section>
    <section class="step step--two">
      <h2 class="step__title">STEP-2</h2>
      <p class="step__text">Find a Dentist</p>
    </section>
    <section class="step step--three">
      <h2 class="step__title">STEP-3</h2>
      <p class="step__text">Get your<br>Appoinment</p>
    </section>

    <div class="brand-mark brand-mark--small">
      <span class="brand-mark__square"></span>
      <span class="brand-mark__name">Molar Relief Fast</span>
    </div>

    <p class="banner-text banner-text--find">FIND A DENTIST IN</p>
    <p class="banner-text banner-text--steps">3 EASY STEPS</p>

    <p class="guarantee">GET SEEN WITHIN 24 HOURS<br><span class="guarantee__or">or</span><br>YOUR MONEY BACK!</p>

    <div class="website-cta">
      <p class="website-cta__lead">SEE OUR WEBSITE FOR FURTHER DETAILS AT</p>
      <p class="website-cta__url">WWW.MOLARRELIEFFAST.NET</p>
    </div>
  </main>
</body>
</html>
```